Electric mountain bike tours nz

We are an Electric Mountain bike tour company in New Zealand. We will be offering bike rental and guided tours around the Nelson region in New Zealand. I want our website to represent both Mountain biking and New Zealand with the colours layout and features. We want tabs for the following:
-1 about us
-2 what we offer
-3 bookings/contact
Under the about us tab will be who we are as a a company. I want the ability to add videos to each of these tabs as we move foward with videos of the tracks we will be riding. I want the website to be editable so I can add and remove videos/photos myself. Also "our bikes" will be under this tab.
Under the what we offer tab will be
-1 bike rental and pricing
-2 guided tours and pricing
-3 recommended package deals.
I want to able to put the tracks under the guided tours tab and select beginner/ intermediate/advanced and have the tracks in each of the following to match the rider level. Also to be able to have a small video of the track would be great in this section.
Bookings and contact tab
(Further information for this tab to be updated soon)
- Silver ferns, kiwi, mountains

```html
<!DOCTYPE html>
<html lang="en">
<head>
<meta charset="utf-8">
<title>Ridgeline – Electric Mountain Bike Tours</title>
<link href="https://fonts.googleapis.com/css2?family=Lato:wght@400;700;900&display=swap" rel="stylesheet">
<style>
:root{
  --ink:#1c1c1c;
  --text:#4a4a4a;
  --muted:#7a7a7a;
  --white:#ffffff;
  --black:#0d0d0d;
  --green:#5ba81e;
  --green-dark:#3f7d10;
  --line:#d6d6d6;
  --grey-bar:#b8b8b8;
}
*{box-sizing:border-box;margin:0;padding:0}
html,body{width:1200px;height:3333px;overflow:hidden;background:var(--white)}
body{position:relative;font-family:'Lato',sans-serif;color:var(--text)}
.abs{position:absolute}
p{line-height:1.55}

/* header */
.site-header{position:absolute;left:0;top:0;width:1200px;height:150px;background:var(--white)}
.brand{position:absolute;left:88px;top:44px;display:flex;align-items:center;gap:12px}
.brand-mark{width:56px;height:56px;border-radius:50%;background:var(--ink)}
.brand-name{font-size:30px;font-weight:900;color:var(--ink);letter-spacing:1px}
.phone-tab{position:absolute;left:845px;top:0;width:355px;height:50px;background:var(--black);border-bottom-left-radius:24px;color:var(--white);display:flex;align-items:center;padding-left:48px;gap:18px;font-size:23px;font-weight:700}
.main-nav{position:absolute;left:540px;top:95px;display:flex;align-items:center;font-size:14px;font-weight:700;color:var(--ink)}
.main-nav span{padding:0 30px;border-left:1px solid var(--line)}
.main-nav span:first-child{border-left:0;padding-left:10px}
.social{display:flex;gap:5px}
.social i{display:block;width:17px;height:17px;border-radius:50%;background:var(--ink)}
.header-social{position:absolute;left:1005px;top:97px}

/* hero */
.hero{position:absolute;left:0;top:150px;width:1200px;height:615px;background:linear-gradient(180deg,#7d94a8 0%,#5f7a8a 35%,#4d6448 70%,#6b6a3e 100%)}
.hero-title{position:absolute;left:0;top:180px;width:1200px;text-align:center;font-size:64px;font-weight:900;color:var(--white)}
.hero-lede{position:absolute;left:225px;top:265px;width:750px;text-align:center;font-size:19px;color:var(--white);line-height:1.35}
.hero-btn{position:absolute;left:532px;top:367px;width:136px;height:42px;border-radius:21px;background:var(--white);color:var(--ink);font-size:15px;font-weight:700;display:flex;align-items:center;justify-content:center}
.hero-arrow{position:absolute;top:250px}

.btn-dark{position:absolute;height:40px;border-radius:20px;background:var(--black);color:var(--white);font-size:14px;font-weight:700;display:flex;align-items:center;justify-content:center}
.btn-light{position:absolute;height:40px;border-radius:20px;background:var(--white);color:var(--ink);font-size:14px;font-weight:700;display:flex;align-items:center;justify-content:center}

.section-title{position:absolute;font-size:28px;font-weight:900}
.section-title .thin{font-weight:400}
.title-rule{position:absolute;height:3px;width:38px}

/* about */
.about-title{left:90px;top:827px;color:var(--ink)}
.about-title .thin{color:var(--muted)}
.about-copy{position:absolute;left:90px;top:898px;width:555px;font-size:14px;text-align:justify}
.video{position:absolute;left:718px;top:905px;width:397px;height:237px;background:linear-gradient(160deg,#b8d0e6,#5d7b9e 55%,#2a3d58)}
.video-bar{position:absolute;left:0;bottom:0;width:100%;height:32px;background:rgba(0,0,0,.7)}

/* bikes */
.bikes{position:absolute;left:0;top:1217px;width:1200px;height:362px;background:linear-gradient(180deg,#3a4a3a,#2b3227 60%,#20241f)}
.bikes-photo{position:absolute;left:145px;top:1340px;width:310px;height:202px;background:linear-gradient(180deg,#8f9a8a,#b3b3ad)}
.bikes-copy{position:absolute;left:612px;top:1335px;width:480px;font-size:14px;color:var(--white);text-align:justify}

/* offer */
.offer{position:absolute;left:0;top:1579px;width:1200px;height:745px;background:linear-gradient(180deg,#23302f,#1b2422 60%,#151b19)}
.offer-col-title{position:absolute;top:1750px;font-size:20px;font-weight:700;color:var(--white)}
.card{position:absolute;top:1802px;width:286px;height:392px;background:var(--white);padding:6px}
.card-photo{width:274px;height:232px}
.card h3{font-size:15px;font-weight:900;color:var(--ink);margin:18px 0 8px 10px}
.card p{font-size:11px;margin:0 10px;color:var(--muted);line-height:1.45;text-align:justify}

/* newsletter */
.newsletter{position:absolute;left:0;top:2325px;width:1200px;height:72px;background:var(--green)}
.nl-label{position:absolute;left:255px;top:18px;font-size:26px;color:var(--white)}
.nl-input{position:absolute;left:533px;top:22px;width:400px;height:30px;background:var(--white);font-size:11px;color:var(--muted);padding:9px 12px}
.nl-btn{position:absolute;left:945px;top:22px;width:132px;height:30px;background:var(--green-dark);color:var(--white);font-size:13px;font-weight:900;display:flex;align-items:center;justify-content:center}

/* blog & testimonials */
.block-title{position:absolute;top:2437px;font-size:26px;font-weight:900;color:var(--ink)}
.pager{position:absolute;top:2443px;display:flex;gap:4px}
.pager i{width:20px;height:20px;border-radius:50%;background:var(--ink);display:block}
.block-rule{position:absolute;top:2497px;height:2px;background:var(--line)}
.post{position:absolute;left:84px;width:480px;display:flex;gap:12px}
.post-thumb{width:84px;height:82px;flex:none}
.post h4{font-size:15px;font-weight:900;color:var(--ink);margin-bottom:5px}
.post p{font-size:12px;color:var(--ink);line-height:1.4}
.divider{position:absolute;left:603px;top:2420px;width:2px;height:330px;background:var(--line)}
.testi-photo{position:absolute;left:657px;top:2535px;width:150px;height:140px;background:linear-gradient(180deg,#a9aeb3,#d9d9d9)}
.testi-name{position:absolute;left:657px;top:2675px;width:150px;height:45px;background:var(--black);color:var(--white);font-size:13px;font-weight:900;display:flex;align-items:center;justify-content:center;letter-spacing:1px}
.testi-copy{position:absolute;left:828px;top:2535px;width:295px;font-size:13px;color:var(--ink);text-align:justify;line-height:1.5}

/* footer */
.footer{position:absolute;left:0;top:2765px;width:1200px;height:502px;background:linear-gradient(180deg,#3a4a55,#27323a 50%,#1b2327)}
.footer-brand{position:absolute;left:160px;top:2915px;display:flex;align-items:center;gap:12px}
.footer-brand .brand-mark{background:var(--white)}
.footer-brand .brand-name{color:var(--white)}
.footer-copy{position:absolute;left:160px;top:3072px;width:230px;font-size:12px;color:var(--white);text-align:justify;line-height:1.45}
.booking{position:absolute;left:455px;top:2888px;width:352px;height:312px;background:var(--white);padding:16px 52px}
.booking h3{text-align:center;font-size:21px;font-weight:900;color:var(--ink);margin-bottom:10px}
.field{border-bottom:1px solid var(--line);font-size:11px;color:var(--muted);padding:10px 0 6px;margin-bottom:8px}
.field.tall{height:58px}
.send{width:78px;height:24px;background:var(--black);color:var(--white);font-size:11px;font-weight:700;display:flex;align-items:center;justify-content:center;margin:12px auto 0}
.contact{position:absolute;left:815px;top:2905px;color:var(--white)}
.contact h3{font-size:21px;font-weight:700;letter-spacing:1px}
.contact .rule{width:150px;height:1px;background:rgba(255,255,255,.5);margin:8px 0 12px}
.contact p{font-size:12px;line-height:1.35}
.contact-line{display:flex;align-items:center;gap:8px;font-size:12px;margin-top:10px}
.follow{font-size:16px;font-weight:900;letter-spacing:1px;margin-top:36px;margin-bottom:14px}
.contact .social i{width:20px;height:20px;background:var(--white)}
.legal{position:absolute;left:0;top:3267px;width:1200px;height:66px;background:var(--grey-bar);display:flex;align-items:center;justify-content:center;font-size:13px;color:var(--ink)}
</style>
</head>
<body>

<header class="site-header">
  <div class="brand"><span class="brand-mark"></span><span class="brand-name">RIDGELINE</span></div>
  <div class="phone-tab">
    <svg width="20" height="28" viewBox="0 0 20 28"><rect x="2" y="1" width="16" height="26" rx="3" fill="none" stroke="#fff" stroke-width="2.5"/><circle cx="10" cy="22" r="1.6" fill="#fff"/></svg>
    (555) 014-2290
  </div>
  <nav class="main-nav"><span>About us</span><span>What we offer</span><span>Bookings/Contact</span></nav>
  <div class="social header-social"><i></i><i></i><i></i><i></i><i></i></div>
</header>

<section class="hero" role="img" aria-label="Two riders on electric mountain bikes overlooking a forested alpine valley">
  <h1 class="hero-title">Ridgeline</h1>
  <p class="hero-lede">We are an Electric Mountain bike tour company in New Zealand. We will be offering bike rental and guided tours around the Nelson region in New Zealand.</p>
  <div class="hero-btn">Read More</div>
  <svg class="hero-arrow" style="left:52px" width="24" height="44" viewBox="0 0 24 44"><path d="M20 4 L4 22 L20 40" fill="none" stroke="rgba(255,255,255,.7)" stroke-width="4"/></svg>
  <svg class="hero-arrow" style="left:1124px" width="24" height="44" viewBox="0 0 24 44"><path d="M4 4 L20 22 L4 40" fill="none" stroke="rgba(255,255,255,.7)" stroke-width="4"/></svg>
</section>

<!-- About -->
<svg class="abs" style="left:132px;top:812px" width="34" height="14" viewBox="0 0 34 14"><path d="M2 13 L12 3 L17 8 L21 4 L32 13" fill="none" stroke="#1c1c1c" stroke-width="2"/></svg>
<h2 class="section-title about-title">About <span class="thin">Us</span></h2>
<div class="title-rule" style="left:90px;top:868px;background:var(--ink)"></div>
<p class="about-copy">Lorem ipsum dolor sit amet, consectetuer adipiscing elit. Aenean commodo ligula eget dolor. Aenean massa. Cum sociis natoque penatibus et magnis dis parturient montes, nascetur ridiculus mus. Donec quam felis, ultricies nec, pellentesque eu, pretium quis, sem. Nulla consequat massa quis enim. Donec pede justo, fringilla vel, aliquet nec, vulputate eget, arcu. In enim justo, rhoncus ut, imperdiet a, venenatis vitae, justo. Nullam dictum felis eu pede mollis pretium. Integer tincidunt. Cras dapibus. Vivamus elementum semper nisi.</p>
<div class="btn-dark" style="left:90px;top:1103px;width:154px">Read More</div>
<div class="video" role="img" aria-label="Video still of a rider descending a snowy forest trail">
  <svg class="abs" style="left:177px;top:90px" width="44" height="44" viewBox="0 0 44 44"><circle cx="22" cy="22" r="21" fill="#fff"/><path d="M17 13 L31 22 L17 31 Z" fill="#1c1c1c"/></svg>
  <div class="video-bar">
    <svg class="abs" style="left:10px;top:10px" width="36" height="14" viewBox="0 0 36 14"><path d="M0 1 L10 7 L0 13 Z" fill="#fff"/><rect x="20" y="1" width="3" height="12" fill="#fff"/><rect x="27" y="1" width="3" height="12" fill="#fff"/></svg>
    <div class="abs" style="left:60px;top:14px;width:320px;height:4px;background:#777"></div>
    <div class="abs" style="left:60px;top:14px;width:120px;height:4px;background:#d62020"></div>
  </div>
</div>

<!-- Our Bikes -->
<section class="bikes" role="img" aria-label="Winding mountain road through grassy hills at dusk"></section>
<svg class="abs" style="left:582px;top:1240px" width="34" height="14" viewBox="0 0 34 14"><path d="M2 13 L12 3 L17 8 L21 4 L32 13" fill="none" stroke="#fff" stroke-width="2"/></svg>
<h2 class="section-title" style="left:0;width:1200px;text-align:center;top:1257px;font-size:25px;color:var(--white);font-weight:700">Our <span class="thin">Bikes</span></h2>
<div class="title-rule" style="left:581px;top:1298px;background:var(--white)"></div>
<div class="bikes-photo" role="img" aria-label="Electric mountain bike parked on an asphalt road"></div>
<p class="bikes-copy">Lorem ipsum dolor sit amet, consectetuer adipiscing elit. Aenean commodo ligula eget dolor. Aenean massa. Cum sociis natoque penatibus et magnis dis parturient montes, nascetur ridiculus mus. Donec quam felis, ultricies nec, pellentesque eu, pretium quis, sem. Nulla consequat massa quis enim. Donec pede justo, fringilla vel, aliquet nec, vulputate eget, arcu.</p>
<div class="btn-dark" style="left:612px;top:1500px;width:154px">Read More</div>

<!-- What we offer -->
<section class="offer" role="img" aria-label="Dark mountain landscape behind the offers"></section>
<svg class="abs" style="left:582px;top:1648px" width="34" height="14" viewBox="0 0 34 14"><path d="M2 13 L12 3 L17 8 L21 4 L32 13" fill="none" stroke="#fff" stroke-width="2"/></svg>
<h2 class="section-title" style="left:0;width:1200px;text-align:center;top:1662px;font-size:27px;color:var(--white);font-weight:700">What we <span class="thin">Offer</span></h2>
<div class="title-rule" style="left:581px;top:1705px;background:var(--white)"></div>

<div class="offer-col-title" style="left:145px">Bike rental &amp; pricing</div>
<div class="offer-col-title" style="left:460px">Guided tours &amp; pricing</div>
<div class="offer-col-title" style="left:770px">Recommended package deals</div>

<article class="card" style="left:146px">
  <div class="card-photo" role="img" aria-label="Mountain bike resting on a hilltop above a sunlit valley" style="background:linear-gradient(180deg,#9fc0dc,#5a7c9e 45%,#3b4a3a)"></div>
  <h3>Lorem ipsum dolor</h3>
  <p>Lorem ipsum dolor sit amet, consectetuer adipiscing elit. Aenean commodo ligula eget dolor. Aenean massa. Cum sociis natoque penatibus et magnis dis parturient montes, nascetur ridiculus mus.</p>
</article>
<article class="card" style="left:459px">
  <div class="card-photo" role="img" aria-label="Two riders with electric bikes on a mountain trail" style="background:linear-gradient(180deg,#8fb0c8,#a89b86 55%,#6c6a5c)"></div>
  <h3>Lorem ipsum dolor</h3>
  <p>Lorem ipsum dolor sit amet, consectetuer adipiscing elit. Aenean commodo ligula eget dolor. Aenean massa. Cum sociis natoque penatibus et magnis dis parturient montes, nascetur ridiculus mus.</p>
</article>
<article class="card" style="left:772px">
  <div class="card-photo" role="img" aria-label="Two cyclists riding a forest path in spring" style="background:linear-gradient(180deg,#a7c784,#6f9a4a 50%,#7d6a4e)"></div>
  <h3>Lorem ipsum dolor</h3>
  <p>Lorem ipsum dolor sit amet, consectetuer adipiscing elit. Aenean commodo ligula eget dolor. Aenean massa. Cum sociis natoque penatibus et magnis dis parturient montes, nascetur ridiculus mus.</p>
</article>
<div class="btn-light" style="left:142px;top:2228px;width:152px">Read More</div>
<div class="btn-light" style="left:461px;top:2228px;width:152px">Read More</div>
<div class="btn-light" style="left:776px;top:2228px;width:152px">Read More</div>

<!-- Newsletter -->
<section class="newsletter">
  <svg class="abs" style="left:197px;top:16px" width="42" height="42" viewBox="0 0 42 42"><circle cx="21" cy="21" r="19" fill="none" stroke="#fff" stroke-width="2"/><rect x="11" y="14" width="20" height="14" rx="1" fill="#fff"/><path d="M11 15 L21 22 L31 15" fill="none" stroke="#5ba81e" stroke-width="2"/></svg>
  <div class="nl-label">News letter Signup</div>
  <svg class="abs" style="left:490px;top:12px" width="20" height="50" viewBox="0 0 20 50"><path d="M3 3 L17 25 L3 47" fill="none" stroke="#fff" stroke-width="2"/></svg>
  <div class="nl-input">Enter Your Email</div>
  <div class="nl-btn">SUBSCRIBE</div>
</section>

<!-- Blog -->
<h2 class="block-title" style="left:84px">Latest Blog</h2>
<div class="pager" style="left:510px"><i></i><i></i></div>
<div class="block-rule" style="left:84px;width:480px"></div>
<div class="post" style="top:2527px">
  <div class="post-thumb" role="img" aria-label="Rider on a forest trail" style="background:linear-gradient(160deg,#86a06a,#4c6a3a)"></div>
  <div><h4>Verum tamen cum de rebus</h4><p>Lorem ipsum dolor sit amet, consectetur adipiscing elit. Quid utem habent admirationis,<br>10-Oct 2017</p></div>
</div>
<div class="post" style="top:2645px">
  <div class="post-thumb" role="img" aria-label="Group of riders resting beside their bikes" style="background:linear-gradient(160deg,#b9a88a,#6c7a8a)"></div>
  <div><h4>Verum tamen cum de rebus</h4><p>Lorem ipsum dolor sit amet, consectetur adipiscing elit. Quid utem habent admirationis,<br>10-Oct 2017</p></div>
</div>
<div class="divider"></div>

<!-- Testimonials -->
<h2 class="block-title" style="left:657px">Testimonials</h2>
<div class="pager" style="left:1077px"><i></i><i></i></div>
<div class="block-rule" style="left:657px;width:460px"></div>
<div class="testi-photo" role="img" aria-label="Portrait of a satisfied customer"></div>
<div class="testi-name">MR HARLOW</div>
<p class="testi-copy"><b style="font-size:20px;line-height:0">&ldquo;</b> Lorem ipsum dolor sit amet, consectetuer adipiscing elit. Aenean commodo ligula eget dolor. Aenean massa. Cum sociis natoque penatibus et magnis dis parturient montes, nascetur ridiculus mus. Donec quam felis, ultricies nec, pellentesque eu, pretium quis, sem. Nulla consequat massa quis enim. Donec pede justo, fringilla vel, aliquet nec, vulputate eget, arcu. In enim justo, rhoncus ut, imperdiet a, venenatis vitae, justo. Nullam dictum felis eu pede mollis pretium. Integer tincidunt. <b style="font-size:20px;line-height:0">&rdquo;</b></p>

<!-- Footer -->
<footer class="footer" role="img" aria-label="Dark mountain range at dusk"></footer>
<div class="footer-brand"><span class="brand-mark"></span><span class="brand-name">RIDGELINE</span></div>
<p class="footer-copy">Lorem ipsum dolor sit amet, consectetuer adipiscing elit. Aenean commodo ligula eget dolor. Aenean massa. Cum sociis natoque penatibus et magnis dis parturient montes, nascetur ridiculus mus. Donec quam felis, ultricies nec, pellentesque eu</p>

<section class="booking">
  <h3>Booking</h3>
  <div class="field">Name</div>
  <div class="field">E-mail</div>
  <div class="field">Phone</div>
  <div class="field tall">Message</div>
  <div class="send">Send</div>
</section>

<section class="contact">
  <h3>Contact</h3>
  <div class="rule"></div>
  <p>42 Harbour Lane<br>Nelson 7010</p>
  <div class="contact-line"><svg width="12" height="12" viewBox="0 0 12 12"><path d="M2 1 L4.5 1 L5.5 3.5 L4 4.8 Q5 7 7.2 8 L8.5 6.5 L11 7.5 L11 10 Q6 11 3 8 Q0.5 5 2 1 Z" fill="#fff"/></svg>555-014-7731</div>
  <div class="contact-line"><svg width="12" height="10" viewBox="0 0 12 10"><rect x="0" y="0" width="12" height="10" fill="#fff"/><path d="M0 1 L6 5.5 L12 1" fill="none" stroke="#27323a" stroke-width="1.2"/></svg>hello@ridgeline.example</div>
  <div class="contact-line"><svg width="12" height="12" viewBox="0 0 12 12"><circle cx="6" cy="6" r="5.5" fill="#fff"/><path d="M0.5 6 H11.5 M6 0.5 V11.5" stroke="#27323a" stroke-width="1"/></svg>www.ridgeline.example</div>
  <div class="follow">FOLLOW US ON</div>
  <div class="social"><i></i><i></i><i></i><i></i><i></i></div>
</section>

<div class="legal">© 2017 ridgeline &nbsp;|&nbsp; Privacy Policy &nbsp;|&nbsp; User Agreement</div>

</body>
</html>
```